OpenCart website

We have an existing site that was based on open cart in 2011 but customised heavily. We want a brand new open cart site designed from scratch so we can work on transitioning the existing opencart database over after the project is done

Current site: www.quillfernstores.com

```html
<!DOCTYPE html>
<html lang="en">
<head>
<meta charset="utf-8">
<title>Quillfern Stores</title>
<link rel="stylesheet" href="https://fonts.googleapis.com/css2?family=Montserrat:wght@400;500;600;700&family=Open+Sans:wght@400;600&display=swap">
<style>
:root{
  --red:#e53935;
  --ink:#222;
  --text:#555;
  --muted:#999;
  --line:#e6e6e6;
  --soft:#f4f4f4;
  --dark:#2b2b2b;
  --white:#fff;
  --tag:#4a90d9;
}
*{box-sizing:border-box;margin:0;padding:0}
html,body{width:1200px;height:3296px;overflow:hidden;background:var(--white)}
body{font-family:"Open Sans",Arial,sans-serif;color:var(--text);font-size:13px;position:relative}
.wrap{width:1080px;margin:0 auto;position:relative}

/* header */
.site-header{height:100px;display:flex;align-items:center;justify-content:space-between;padding:0 60px;position:relative}
.nav{display:flex;gap:26px;font-family:"Montserrat",sans-serif;font-size:12px;font-weight:600;color:var(--ink);letter-spacing:.5px}
.nav .active{color:var(--red)}
.nav-left{margin-left:70px}
.search-icon{position:absolute;left:62px;top:42px}
.brand-name{position:absolute;left:50%;top:50%;transform:translate(-50%,-50%);font-family:"Montserrat",sans-serif;font-weight:700;font-size:26px;color:var(--red);letter-spacing:.5px}
.nav-right{display:flex;align-items:center}
.header-icons{display:flex;gap:18px;align-items:center;margin-left:40px}

/* hero */
.hero{height:440px;position:relative;background:linear-gradient(90deg,#f1f1f1 0%,#e9e9e9 45%,#dcdcdc 100%);overflow:hidden}
.hero-photo{position:absolute;right:0;top:0;width:720px;height:440px;background:linear-gradient(90deg,rgba(236,236,236,0) 0%,#8a8a8a 35%,#3a3a3a 60%,#5a5a5a 85%,#cfcfcf 100%)}
.hero-copy{position:absolute;left:260px;top:102px}
.hero-kicker{font-family:"Montserrat",sans-serif;font-size:22px;font-weight:600;letter-spacing:3px;color:var(--ink)}
.hero-title{font-family:"Montserrat",sans-serif;font-size:48px;font-weight:500;color:var(--red);margin-top:10px}
.hero-sub{font-size:14px;color:var(--text);margin-top:6px}
.btn{display:inline-block;border:1px solid var(--ink);font-family:"Montserrat",sans-serif;font-size:11px;font-weight:600;letter-spacing:1px;color:var(--ink);padding:9px 22px}
.hero .btn{margin-top:26px;margin-left:12px}
.arrow{position:absolute;top:205px}

/* features */
.features{height:140px;display:flex;justify-content:center;gap:200px;align-items:center;border-bottom:1px solid var(--line)}
.feature{text-align:center}
.feature h4{font-family:"Montserrat",sans-serif;font-size:13px;font-weight:600;color:var(--ink);margin-top:8px}
.feature p{font-size:10px;color:var(--muted);letter-spacing:1px;margin-top:3px}

/* section title */
.section-title{text-align:center;font-family:"Montserrat",sans-serif;font-size:28px;font-weight:500;color:var(--ink)}
.tabs{display:flex;justify-content:center;gap:16px;font-family:"Montserrat",sans-serif;font-size:10px;font-weight:600;color:var(--muted);letter-spacing:.5px;margin-top:18px}
.tabs .active{color:var(--red)}
.title-row{position:relative;padding-top:58px}
.title-row .rule{position:absolute;top:74px;height:1px;background:var(--line);width:340px}

/* products */
.products{display:grid;grid-template-columns:repeat(5,1fr);gap:22px;margin-top:36px}
.card{text-align:center;position:relative}
.thumb{height:250px;border:1px solid var(--line);position:relative;background:var(--white)}
.thumb-fill{position:absolute;left:28px;right:28px;top:24px;bottom:24px}
.fill-duster{background:linear-gradient(160deg,#fbe3e0 0%,#fdf3d9 35%,#e2f1e2 65%,#e3ebf8 100%)}
.fill-pan{background:linear-gradient(180deg,#d9d9d9 0%,#bdbdbd 55%,#f4d3b5 100%)}
.fill-wipes{background:linear-gradient(180deg,#dbe8f7 0%,#f6dada 40%,#dcefdc 70%,#f8f1cf 100%)}
.fill-dish{background:linear-gradient(135deg,#eef1f3 0%,#d5dde2 55%,#f1d3d3 100%)}
.fill-opener{background:linear-gradient(180deg,#f6f6f6 0%,#e0e0e0 45%,#bdbdbd 100%)}
.tag{position:absolute;left:8px;top:8px;background:var(--tag);color:#fff;font-size:9px;font-weight:600;padding:4px 6px;z-index:1}
.card .cat{font-size:9px;color:var(--muted);letter-spacing:1px;margin-top:14px}
.card .name{font-size:12px;color:var(--ink);margin-top:6px}
.card .price{font-family:"Montserrat",sans-serif;font-size:14px;font-weight:600;color:var(--red);margin-top:8px}
.card .price s{color:var(--muted);font-weight:400;margin-right:8px}
.actions{position:absolute;left:50%;transform:translateX(-50%);bottom:10px;display:flex;gap:8px;z-index:1}
.actions span{width:30px;height:30px;border-radius:50%;border:1px solid var(--line);background:#fff;display:block}
.actions span:first-child{background:var(--red);border-color:var(--red)}

/* promo */
.promos{display:grid;grid-template-columns:1fr 1fr;gap:36px;margin-top:110px}
.promo{height:330px;position:relative;overflow:hidden}
.promo-home{background:linear-gradient(135deg,#8a8a8a 0%,#c9c9c9 45%,#6f6f6f 100%)}
.promo-beauty{background:linear-gradient(135deg,#d9d9d9 0%,#8e8e8e 60%,#bcbcbc 100%)}
.promo-copy{position:absolute;left:90px;top:100px;color:#fff}
.promo-copy small{font-family:"Montserrat",sans-serif;font-size:12px;letter-spacing:2px;font-weight:600}
.promo-copy h3{font-family:"Montserrat",sans-serif;font-size:34px;font-weight:500;margin-top:6px}
.promo-copy .btn{border-color:#fff;color:#fff;margin-top:14px;padding:7px 16px;font-size:10px}

/* three lists */
.tri-heads{display:grid;grid-template-columns:1fr 1fr 1fr;margin-top:80px;text-align:center;position:relative}
.tri-heads::before{content:"";position:absolute;left:0;right:0;top:11px;height:1px;background:var(--line)}
.tri-heads h3{font-family:"Montserrat",sans-serif;font-size:18px;font-weight:600;color:var(--ink);letter-spacing:1px;position:relative}
.tri-heads h3 span{background:#fff;padding:0 18px}
.products.lower{margin-top:40px}
.products.lower .thumb{height:210px}

/* blog */
.blog{background:var(--soft);height:600px;margin-top:70px;position:relative}
.blog .section-title{padding-top:48px}
.blog-sub{text-align:center;font-size:10px;color:var(--muted);margin-top:8px}
.blog-body{display:grid;grid-template-columns:560px 1fr;gap:40px;margin-top:30px}
.blog-feature{height:330px;background:linear-gradient(160deg,#b7b7b7 0%,#6b6b6b 50%,#3a3a3a 100%);position:relative}
.blog-feature .overlay{position:absolute;left:24px;bottom:24px;color:#fff}
.blog-feature .date{font-size:10px;letter-spacing:1px}
.blog-feature h4{font-family:"Montserrat",sans-serif;font-size:20px;font-weight:600;line-height:1.3;margin-top:6px;width:440px}
.post{border-bottom:1px solid #ddd;padding:18px 0}
.post:first-child{padding-top:8px}
.post:last-child{border-bottom:0}
.post .date{font-size:10px;color:var(--red);letter-spacing:1px}
.post p{font-size:14px;line-height:1.6;color:var(--text);margin-top:6px}
.post p.hot{color:var(--red)}
.blog .btn{position:absolute;left:50%;transform:translateX(-50%);bottom:42px;background:#fff;padding:8px 20px;font-size:10px}

/* brands */
.brands{height:200px;display:flex;align-items:center;padding-left:60px;gap:40px}
.brands-label{font-family:"Montserrat",sans-serif;font-size:22px;font-weight:700;color:var(--ink);line-height:1.1;width:110px}
.brands-arrow{margin-left:-30px}
.brand-box{width:190px;height:100px;border:1px solid var(--line);display:flex;align-items:center;justify-content:center}
.brand-box span{width:60px;height:40px;background:#cfcfcf;border-radius:4px}

/* footer */
.site-footer{position:absolute;left:0;right:0;top:2940px;height:356px;background:var(--dark);color:#bbb}
.footer-cols{display:grid;grid-template-columns:460px 230px 230px 1fr;padding:56px 60px 0 60px}
.footer-cols h5{font-family:"Montserrat",sans-serif;font-size:14px;color:#fff;font-weight:600;margin-bottom:18px}
.footer-cols li{list-style:none;font-size:12px;line-height:22px}
.phone{font-family:"Montserrat",sans-serif;font-size:26px;color:#fff;font-weight:500}
.mail{font-size:12px;margin-top:6px}
.socials{display:flex;gap:12px;margin-top:18px}
.socials span{width:14px;height:14px;border-radius:50%;background:#999}
.subscribe{display:flex;border-bottom:1px solid #666;width:200px;justify-content:space-between;padding:6px 0;font-size:11px;color:#888}
.subscribe-note{font-size:10px;color:#888;margin-top:10px;width:200px;line-height:1.5}
.footer-bottom{position:absolute;left:60px;right:60px;bottom:30px;display:flex;justify-content:space-between;align-items:center;border-top:1px solid #444;padding-top:22px;font-size:11px;color:#888}
.cards{display:flex;gap:8px}
.cards span{width:34px;height:22px;border:1px solid #777;border-radius:3px}
</style>
</head>
<body>

<header class="site-header">
  <svg class="search-icon" width="16" height="16" viewBox="0 0 16 16" fill="none" stroke="#222" stroke-width="1.6"><circle cx="6.5" cy="6.5" r="5"/><path d="M10.5 10.5 15 15"/></svg>
  <nav class="nav nav-left">
    <span class="active">HOME</span><span>BRANDS</span><span>NEW</span><span>SALE</span>
  </nav>
  <div class="brand-name">Quillfern Stores</div>
  <div class="nav-right">
    <nav class="nav"><span>ABOUT</span><span>BLOG</span><span>CONTACT</span></nav>
    <div class="header-icons">
      <svg width="16" height="16" viewBox="0 0 16 16" fill="none" stroke="#222" stroke-width="1.5"><circle cx="8" cy="5" r="3.5"/><path d="M1.5 15c1-4 12-4 13 0"/></svg>
      <svg width="20" height="18" viewBox="0 0 20 18" fill="none" stroke="#222" stroke-width="1.5"><path d="M1 1h3l2 10h11l2-7H5"/><circle cx="8" cy="15.5" r="1.3"/><circle cx="15" cy="15.5" r="1.3"/></svg>
    </div>
  </div>
</header>

<section class="hero">
  <div class="hero-photo" role="img" aria-label="Black cast-iron casserole pots stacked with a wooden-handled pan on a light surface"></div>
  <svg class="arrow" style="left:20px" width="20" height="30" viewBox="0 0 20 30" fill="none" stroke="#666" stroke-width="2"><path d="M14 4 4 15l10 11"/></svg>
  <svg class="arrow" style="right:20px" width="20" height="30" viewBox="0 0 20 30" fill="none" stroke="#eee" stroke-width="2"><path d="M6 4l10 11L6 26"/></svg>
  <div class="hero-copy">
    <div class="hero-kicker">COOKWARE</div>
    <div class="hero-title">Up to 20% Off</div>
    <div class="hero-sub">Big Savings on Big Brands!</div>
    <span class="btn">SHOP NOW</span>
  </div>
</section>

<section class="features">
  <div class="feature">
    <svg width="30" height="26" viewBox="0 0 30 26" fill="none" stroke="#444" stroke-width="1.6"><path d="M4 16v-4a11 11 0 0 1 22 0v4"/><rect x="2" y="14" width="5" height="8" rx="1"/><rect x="23" y="14" width="5" height="8" rx="1"/></svg>
    <h4>Support Customer</h4><p>SUPPORT 24/7</p>
  </div>
  <div class="feature">
    <svg width="34" height="26" viewBox="0 0 34 26" fill="none" stroke="#444" stroke-width="1.6"><path d="M2 4h18v14H2zM20 9h7l5 5v4H20"/><circle cx="8" cy="20" r="3"/><circle cx="26" cy="20" r="3"/></svg>
    <h4>Free shipping</h4><p>ON ORDER OVER $99</p>
  </div>
  <div class="feature">
    <svg width="32" height="26" viewBox="0 0 32 26" fill="none" stroke="#444" stroke-width="1.6"><rect x="2" y="4" width="28" height="18" rx="2"/><path d="M2 10h28M6 17h8"/></svg>
    <h4>Payment security</h4><p>100% SECURE</p>
  </div>
</section>

<main class="wrap">
  <div class="title-row">
    <span class="rule" style="left:0"></span><span class="rule" style="right:0"></span>
    <h2 class="section-title">Quillfern Stores</h2>
    <div class="tabs"><span class="active">ALL</span><span>CLEANING</span><span>COOK</span><span>CRAFTS</span><span>GLASS</span><span>HARDWARE</span><span>KITCHEN</span><span>ACCESSORIES</span></div>
  </div>

  <div class="products">
    <div class="card">
      <div class="thumb"><div class="thumb-fill fill-duster" role="img" aria-label="Product photo: rainbow feather duster"></div></div>
      <div class="cat">WALL STICKER</div><div class="name">Duster Feather 20" Multiful</div><div class="price">$29.00</div>
    </div>
    <div class="card">
      <div class="thumb"><span class="tag">NEW</span><div class="thumb-fill fill-pan" role="img" aria-label="Product photo: non-stick fry pan with orange handle"></div></div>
      <div class="cat">WALL STICKER</div><div class="name">Fry Pan 8" Non Stick Induction</div><div class="price">$92.00</div>
    </div>
    <div class="card">
      <div class="thumb"><div class="thumb-fill fill-wipes" role="img" aria-label="Product photo: packaged multicolour paper wipes"></div>
        <div class="actions"><span></span><span></span><span></span></div></div>
      <div class="cat">WALL STICKER</div><div class="name">Multi Color Paper Mini High Density</div><div class="price">$37.00</div>
    </div>
    <div class="card">
      <div class="thumb"><div class="thumb-fill fill-dish" role="img" aria-label="Product photo: clear glass baking dish in box"></div></div>
      <div class="cat">WALL STICKER</div><div class="name">Clearbake Dish Baking Oblong 4.8qt Clear</div><div class="price"><s>$19.00</s>$37.00</div>
    </div>
    <div class="card">
      <div class="thumb"><div class="thumb-fill fill-opener" role="img" aria-label="Product photo: one-handed bottle opener on card"></div></div>
      <div class="cat">WALL STICKER</div><div class="name">Axle one-handed bottle opener</div><div class="price">$18.00</div>
    </div>
  </div>

  <div class="promos">
    <div class="promo promo-home" role="img" aria-label="Overhead view of pots, pans and kitchen utensils">
      <div class="promo-copy"><small>UP TO 20% OFF</small><h3>Home &amp; Kitchen</h3><span class="btn">SHOP NOW</span></div>
    </div>
    <div class="promo promo-beauty" role="img" aria-label="Makeup brushes and eyeshadow palette">
      <div class="promo-copy" style="left:110px"><small>UP TO 30% OFF</small><h3>Health &amp; Beauty</h3><span class="btn">SHOP NOW</span></div>
    </div>
  </div>

  <div class="tri-heads">
    <h3><span>NEW ARRIVAL</span></h3><h3><span>CLEARANCE SALE</span></h3><h3><span>BEST SELLERS</span></h3>
  </div>

  <div class="products lower">
    <div class="card">
      <div class="thumb"><div class="thumb-fill fill-duster" role="img" aria-label="Product photo: rainbow feather duster"></div></div>
      <div class="cat">WALL STICKER</div><div class="name">Duster Feather 20" Multiful</div><div class="price">$29.00</div>
    </div>
    <div class="card">
      <div class="thumb"><div class="thumb-fill fill-pan" role="img" aria-label="Product photo: non-stick fry pan with orange handle"></div></div>
      <div class="cat">WALL STICKER</div><div class="name">Fry Pan 8" Non Stick Induction</div><div class="price">$92.00</div>
    </div>
    <div class="card">
      <div class="thumb"><div class="thumb-fill fill-wipes" role="img" aria-label="Product photo: packaged multicolour paper wipes"></div></div>
      <div class="cat">WALL STICKER</div><div class="name">Multi Color Paper Mini High Density</div><div class="price">$37.00</div>
    </div>
    <div class="card">
      <div class="thumb"><div class="thumb-fill fill-dish" role="img" aria-label="Product photo: clear glass baking dish in box"></div></div>
      <div class="cat">WALL STICKER</div><div class="name">Clearbake Dish Baking Oblong 4.8qt Clear</div><div class="price"><s>$19.00</s>$37.00</div>
    </div>
    <div class="card">
      <div class="thumb"><div class="thumb-fill fill-opener" role="img" aria-label="Product photo: one-handed bottle opener on card"></div></div>
      <div class="cat">WALL STICKER</div><div class="name">Axle one-handed bottle opener</div><div class="price">$18.00</div>
    </div>
  </div>
</main>

<section class="blog">
  <h2 class="section-title">Latest Blog Post</h2>
  <p class="blog-sub">Simple Design, Smart Products. The perfect choice for you.</p>
  <div class="wrap blog-body">
    <article class="blog-feature" role="img" aria-label="Shoppers walking with bags on a city street">
      <div class="overlay"><div class="date">05 APR, 2018</div><h4>Dong ac elit a ante commodo condimentum a vehicula dummy text</h4></div>
    </article>
    <div class="posts">
      <div class="post"><div class="date">05 APR, 2018</div><p>It is a long established fact that a reader will be distracted by the readable content.</p></div>
      <div class="post"><div class="date">05 APR, 2018</div><p class="hot">Contrary to popular belief, Lorem Ipsum is not simply random text. It has roots in a piece.</p></div>
      <div class="post"><div class="date">05 APR, 2018</div><p>Sed ut perspiciatis unde omnis iste natus error sit voluptatem accusantium doloremque.</p></div>
    </div>
  </div>
  <span class="btn">VIEW ALL</span>
</section>

<section class="brands">
  <div class="brands-label">TOP<br>BRANDS</div>
  <svg class="brands-arrow" width="14" height="40" viewBox="0 0 14 40" fill="none" stroke="#ccc" stroke-width="1.5"><path d="M2 2l10 18L2 38"/></svg>
  <div class="brand-box" role="img" aria-label="Partner brand"><span></span></div>
  <div class="brand-box" role="img" aria-label="Partner brand"><span></span></div>
  <div class="brand-box" role="img" aria-label="Partner brand"><span></span></div>
  <div class="brand-box" role="img" aria-label="Partner brand"><span></span></div>
</section>

<footer class="site-footer">
  <div class="footer-cols">
    <div>
      <h5>Quillfern Stores</h5>
      <div class="phone">P. 1 (555) - 014 - 2290</div>
      <div class="mail">E. info@quillfernstores.com</div>
      <div class="socials"><span></span><span></span><span></span><span></span></div>
    </div>
    <div>
      <h5>Quick Link</h5>
      <ul><li>About</li><li>Blog</li><li>Privacy Policy</li><li>Terms &amp; conditions</li><li>Sitemap</li><li>Contact</li><li>FAQ</li></ul>
    </div>
    <div>
      <h5>Quick Link</h5>
      <ul><li>Shop</li><li>Brand</li><li>New</li><li>Sale</li></ul>
    </div>
    <div>
      <h5>Get 20% Off</h5>
      <div class="subscribe"><span>Your email address</span>
        <svg width="14" height="10" viewBox="0 0 14 10" fill="none" stroke="#bbb" stroke-width="1.4"><path d="M0 5h12M8 1l4 4-4 4"/></svg></div>
      <p class="subscribe-note">By subscribing you agree to our newsletter terms.</p>
    </div>
  </div>
  <div class="footer-bottom">
    <span>© 2018 Quillfern Stores. All Rights Reserved.</span>
    <div class="cards"><span></span><span></span><span></span><span></span><span></span></div>
  </div>
</footer>

</body>
</html>
```